Business Cards

Business card design for my company.
I would like the card's background colour to be black. You can also see our web site to get an idea of our brand. https://www.dlqmarrowfield.com.au/
- Name
- Email

```html
<!DOCTYPE html>
<html lang="en">
<head>
<meta charset="UTF-8">
<title>DLQ Marrowfield Business Cards</title>
<link href="https://fonts.googleapis.com/css2?family=Archivo+Black&family=Montserrat:wght@500;600;700&display=swap" rel="stylesheet">
<style>
  :root {
    --backdrop: #2b2b2b;
    --card: #050505;
    --edge: #1f9a48;
    --green: #23a84f;
    --white: #f2f2f2;
  }
  * { box-sizing: border-box; margin: 0; padding: 0; }
  html, body { width: 1200px; height: 939px; overflow: hidden; }
  body {
    background: var(--backdrop);
    position: relative;
    font-family: "Montserrat", sans-serif;
    color: var(--white);
  }
  .card {
    position: absolute;
    width: 560px;
    height: 320px;
    background: var(--card);
    border-left: 3px solid var(--edge);
    border-bottom: 3px solid var(--edge);
    box-shadow: 0 14px 30px rgba(0,0,0,0.45);
  }
  .card--front { left: 60px; top: 110px; }
  .card--back { left: 580px; top: 500px; }

  .brand {
    display: flex;
    align-items: center;
    gap: 12px;
    font-family: "Montserrat", sans-serif;
    font-weight: 700;
    color: var(--white);
    letter-spacing: 0.14em;
    text-transform: uppercase;
  }
  .brand__mark { background: var(--green); flex: none; }

  .card--front .brand {
    position: absolute;
    left: 50%; top: 50%;
    transform: translate(-50%, -50%);
    font-size: 30px;
    white-space: nowrap;
  }
  .card--front .brand__mark { width: 22px; height: 22px; }

  .card--back .brand {
    position: absolute;
    right: 34px; top: 40px;
    font-size: 17px;
    gap: 9px;
    white-space: nowrap;
  }
  .card--back .brand__mark { width: 13px; height: 13px; }

  .holder {
    position: absolute;
    left: 40px; bottom: 34px;
  }
  .holder__name {
    font-family: "Archivo Black", sans-serif;
    font-size: 30px;
    font-weight: 400;
    letter-spacing: 0.02em;
    text-transform: uppercase;
    line-height: 1.05;
  }
  .holder__role {
    color: var(--green);
    font-weight: 600;
    font-size: 15px;
    margin-top: 2px;
  }
  .holder__rule {
    width: 220px;
    height: 2px;
    background: var(--white);
    margin: 8px 0 10px;
  }
  .contacts { list-style: none; }
  .contacts li {
    display: flex;
    align-items: center;
    gap: 10px;
    font-size: 14px;
    font-weight: 500;
    line-height: 1.55;
    white-space: nowrap;
  }
  .contacts svg { width: 13px; height: 13px; fill: var(--green); flex: none; }
</style>
</head>
<body>
  <section class="card card--front">
    <div class="brand"><span class="brand__mark"></span>DLQ Marrowfield</div>
  </section>

  <section class="card card--back">
    <div class="brand"><span class="brand__mark"></span>DLQ Marrowfield</div>
    <div class="holder">
      <h1 class="holder__name">Colin Hartley</h1>
      <p class="holder__role">General Manager</p>
      <div class="holder__rule"></div>
      <ul class="contacts">
        <li>
          <svg viewBox="0 0 24 24" aria-hidden="true"><path d="M6.6 10.8a15.1 15.1 0 0 0 6.6 6.6l2.2-2.2a1 1 0 0 1 1-.25 11.4 11.4 0 0 0 3.6.57 1 1 0 0 1 1 1V20a1 1 0 0 1-1 1A17 17 0 0 1 3 4a1 1 0 0 1 1-1h3.5a1 1 0 0 1 1 1c0 1.25.2 2.45.57 3.57a1 1 0 0 1-.25 1z"/></svg>
          0400 555 018
        </li>
        <li>
          <svg viewBox="0 0 24 24" aria-hidden="true"><path d="M2 5h20v14H2z M3.5 6.5 12 13l8.5-6.5" fill="none" stroke="#23a84f" stroke-width="2"/><path d="M2 5h20L12 12.5z"/></svg>
          info@dlqmarrowfield.com.au
        </li>
        <li>
          <svg viewBox="0 0 24 24" aria-hidden="true"><circle cx="12" cy="12" r="9.5" fill="none" stroke="#23a84f" stroke-width="2"/><path d="M2.5 12h19M12 2.5c3 3 3 16 0 19M12 2.5c-3 3-3 16 0 19" fill="none" stroke="#23a84f" stroke-width="1.6"/></svg>
          www.dlqmarrowfield.com.au
        </li>
        <li>
          <svg viewBox="0 0 24 24" aria-hidden="true"><path d="M12 2a7 7 0 0 0-7 7c0 5.3 7 13 7 13s7-7.7 7-13a7 7 0 0 0-7-7zm0 9.5A2.5 2.5 0 1 1 12 6.5a2.5 2.5 0 0 1 0 5z"/></svg>
          Arlowe Creek, Tasmania, Australia
        </li>
      </ul>
    </div>
  </section>
</body>
</html>
```